~~ Night Club Website ~~

We would like to redo our website for Halo Velvet Room (http://www.halovelvetroom-example.com).

Halo Velvet Room is Edmonton's #1 electronic dance music night club.

We have DJs that fly in from around the world to play at our club and want to be able to properly showcase our upcoming shows and events to increase sales.
Updates

I have now guaranteed the project.  Let's see some brilliant designs!

Target Market(s)

Electronic Dance Music Lovers; College / University Students; Young Professionals

Industry/Entity Type

Electronic

Requirements
Must have
• The site must have the following sections:

1. Home Page
- Rotating Banner where we can put upcoming events
- Twitter, Facebook, YouTube, FourSquare buttons
- Our Twitter feed to automatically post
- Facebook integration with 'Like' and Comments for upcoming shows
- An email signup section for contests and giveaways that auto-updates the email list in MailChimp
- Streaming music from 9 Pulse Radio

2. Photos
- This needs to integrate right into our Facebook Albums

3. Weekly Lineup

4. Events
- People need to be able to buy tickets right online via PayPal

5. Bookings
- People need to be able to pick a party package and pay right online via PayPal

6. Contact Us

```html
<!DOCTYPE html>
<html lang="en">
<head>
<meta charset="utf-8">
<title>Halo Velvet Room</title>
<link href="https://fonts.googleapis.com/css2?family=PT+Sans:wght@400;700&display=swap" rel="stylesheet">
<style>
:root{
  --black:#0b0b0b;
  --white:#ffffff;
  --panel:#dddde0;
  --navy:#0f2a6e;
  --text:#333333;
  --rule:#b5b5b8;
  --dark-box:#4a4a4a;
  --dark-tab:#8a8a8a;
  --field-dark:#5c5c5c;
  --orange:#f26a10;
  --orange-top:#ff8a2a;
  --nav-border:#2e2e2e;
  --field-light:#f4f4f6;
  --field-border:#cfcfd3;
  --cyan:#2cb4e8;
}
*{margin:0;padding:0;box-sizing:border-box}
html,body{width:1200px;height:1077px;overflow:hidden;background:var(--white)}
body{position:relative;font-family:"PT Sans",Arial,sans-serif;color:var(--text)}
.abs{position:absolute}

/* header */
.site-header{left:0;top:0;width:1200px;height:143px;background:var(--black)}
.brand{left:188px;top:52px;width:110px;color:var(--white);font-size:17px;line-height:19px;letter-spacing:2px;text-align:center;display:flex;flex-direction:column;align-items:center;gap:6px}
.brand-mark{width:14px;height:14px;background:var(--cyan)}
.like-btn{left:629px;top:35px;width:43px;height:20px;border:1px solid #999;border-radius:3px;background:#e9e9e9;color:#222;font-size:10px;line-height:18px;text-align:center}
.like-note{left:680px;top:40px;color:#cfcfcf;font-size:9.5px}
.follow{left:856px;top:40px;color:#e4e4e4;font-size:12px}
.social{top:37px;width:22px;height:22px;border-radius:3px}
.main-nav{left:344px;top:90px;width:671px;height:31px;border:1px solid var(--nav-border);border-radius:6px;display:flex;align-items:center}
.main-nav a{flex:1;color:var(--white);text-decoration:none;font-size:12px;text-align:center;border-right:1px solid var(--nav-border);line-height:20px}
.main-nav a:last-child{border-right:none}

/* hero */
.hero{left:172px;top:159px;width:859px;height:302px;background:radial-gradient(ellipse at 60% 30%,#3fd7f5 0%,#1f5fd8 30%,#14206b 65%,#07091e 100%)}
.hero-shadow{left:200px;top:461px;width:800px;height:12px;background:radial-gradient(ellipse at 50% 0,rgba(0,0,0,.35),rgba(0,0,0,0) 70%)}
.dots{left:905px;top:429px;display:flex;gap:6px}
.dots span{width:11px;height:11px;border-radius:50%;background:var(--white)}
.dots span.on{background:var(--cyan)}

/* welcome */
.welcome{left:171px;top:486px;width:858px;height:191px;background:var(--panel)}
.h2{color:var(--navy);font-size:17px;font-weight:400}
.welcome .h2{left:25px;top:17px}
.welcome .rule{left:16px;top:47px;width:534px;height:1px;background:var(--rule)}
.welcome p{left:24px;top:68px;width:523px;font-size:11.6px;line-height:20.3px;text-align:justify}
.signup{left:583px;top:17px;width:257px;height:137px;background:var(--dark-box);border-radius:8px}
.signup-tab{left:11px;top:10px;width:25px;height:114px;background:var(--dark-tab);border-radius:6px}
.signup-tab span{position:absolute;left:50%;top:50%;transform:translate(-50%,-50%) rotate(-90deg);color:var(--white);font-size:16px;white-space:nowrap}
.dark-field{left:48px;width:193px;height:30px;background:var(--field-dark);border-radius:8px;color:#e6e6e6;font-size:11px;line-height:30px;padding-left:14px;box-shadow:inset 0 1px 2px rgba(0,0,0,.4)}
.btn{background:linear-gradient(var(--orange-top),var(--orange));color:var(--white);text-align:center}
.signin{left:177px;top:108px;width:62px;height:22px;border-radius:8px;font-size:13px;line-height:22px;color:#111}

/* columns */
.col-title{top:700px}
.col-rule{top:729px;height:1px;background:var(--rule)}
.arrow{top:707px}
.thumb{width:69px;height:69px}
.specials{left:473px;top:745px;width:290px;font-size:11.6px;line-height:14px;color:#222}
.specials p{margin-bottom:11px}
.light-field{left:777px;width:252px;border:1px solid var(--field-border);background:linear-gradient(var(--white),var(--field-light));font-size:10.5px;color:#555;padding:6px 11px}
.submit{left:958px;top:928px;width:70px;height:27px;font-size:14px;line-height:27px}

/* footer */
.site-footer{left:0;top:976px;width:1200px;height:101px;background:var(--black);color:var(--white)}
.foot-nav{right:177px;top:30px;font-size:12px;display:flex;gap:0}
.foot-nav a{color:var(--white);text-decoration:none;padding:0 10px;border-right:1px solid #bbb;line-height:13px}
.foot-nav a:last-child{border-right:none;padding-right:0}
.copyright{right:176px;top:55px;font-size:12px}
</style>
</head>
<body>

<header class="site-header abs">
  <div class="brand abs"><span class="brand-mark"></span><span>HALO VELVET ROOM</span></div>
  <div class="like-btn abs">Like</div>
  <div class="like-note abs">Be the first of your friends to like this</div>
  <div class="follow abs">Follow Us</div>
  <div class="social abs" style="left:915px;background:#3b5ea8" aria-label="Social link"></div>
  <div class="social abs" style="left:942px;background:#c4302b" aria-label="Video link"></div>
  <div class="social abs" style="left:969px;background:#3fb0e6" aria-label="Microblog link"></div>
  <div class="social abs" style="left:997px;background:#5fb8e0" aria-label="Check-in link"></div>
  <nav class="main-nav abs">
    <a href="#">Home</a><a href="#">Photos</a><a href="#">Weekly Specials</a><a href="#">Events</a><a href="#">Bookings</a><a href="#">Contact Us</a>
  </nav>
</header>

<div class="hero abs" role="img" aria-label="Crowd dancing with raised hands under blue club lights"></div>
<div class="dots abs"><span></span><span class="on"></span><span></span><span></span><span></span><span></span></div>
<div class="hero-shadow abs"></div>

<section class="welcome abs">
  <h2 class="h2 abs">Welcome to Our Site</h2>
  <div class="rule abs"></div>
  <p class="abs">Enjoy friendly service from when you first arrive at the door and throughout your night from our bartend-ers and servers. Our collection of well known Resident DJ’s will be spinning your favorite tracks and guid-ing your musical entertainment in House, Dirty Electro, and funky Mashups. Dress to impress and relax with friends in one of our VIP booths and receive personalized bottle service - Please call ahead to make reservations</p>
  <div class="signup abs">
    <div class="signup-tab abs"><span>Sign Up</span></div>
    <div class="dark-field abs" style="top:22px">E mail id</div>
    <div class="dark-field abs" style="top:63px">Password</div>
    <div class="signin btn abs">Sign In</div>
  </div>
</section>

<h2 class="h2 col-title abs" style="left:173px">Photo Gallery</h2>
<svg class="arrow abs" style="left:397px" width="30" height="14" viewBox="0 0 30 14"><path d="M7 2 L2 7 L7 12 M23 2 L28 7 L23 12" fill="none" stroke="#222" stroke-width="2"/></svg>
<div class="col-rule abs" style="left:173px;width:252px"></div>
<div class="thumb abs" style="left:178px;top:753px;background:linear-gradient(135deg,#b8d83a,#3a4a20)" role="img" aria-label="Party photo"></div>
<div class="thumb abs" style="left:264px;top:753px;background:linear-gradient(135deg,#2a2a5a,#7a3040)" role="img" aria-label="Party photo"></div>
<div class="thumb abs" style="left:352px;top:753px;background:linear-gradient(135deg,#2a3aa0,#201018)" role="img" aria-label="Party photo"></div>
<div class="thumb abs" style="left:179px;top:837px;background:linear-gradient(135deg,#3040b0,#1a1a2a)" role="img" aria-label="Party photo"></div>
<div class="thumb abs" style="left:265px;top:837px;background:linear-gradient(135deg,#3a3ab8,#2a1a1a)" role="img" aria-label="Party photo"></div>
<div class="thumb abs" style="left:354px;top:835px;background:linear-gradient(135deg,#2a40c8,#141428)" role="img" aria-label="Party photo"></div>

<h2 class="h2 col-title abs" style="left:472px">Weekely Specials</h2>
<div class="col-rule abs" style="left:472px;width:253px"></div>
<div class="specials abs">
  <p>Wednesday:<br>Halo 4th Annual Spin Off $4 Highballs,<br>$4 Domestic Beers,$99 Bottles</p>
  <p>Thursday:<br>Closed (Open For Special Events &amp; DJ Shows)<br>Promoters Email jordan@halovelvetroom-example.com</p>
  <p>Friday:<br>Velvet Bassline Fridays - $4 Amaro and Pinecrest</p>
  <p>Saturday:<br>Neonlight Saturdays - $4 Lager &amp; Dark Rum - Rico Vance and his lineup of guest DJs dropping mad beats all night long!</p>
</div>

<h2 class="h2 col-title abs" style="left:775px">Booking</h2>
<div class="col-rule abs" style="left:775px;width:253px"></div>
<div class="light-field abs" style="top:747px;height:28px">Name</div>
<div class="light-field abs" style="top:780px;height:28px">E mail</div>
<div class="light-field abs" style="top:813px;height:29px">Date</div>
<div class="light-field abs" style="top:848px;height:67px;padding-top:9px">Message</div>
<div class="submit btn abs">Submit</div>

<footer class="site-footer abs">
  <nav class="foot-nav abs">
    <a href="#">Home</a><a href="#">Photos</a><a href="#">Weekly Specials</a><a href="#">Events</a><a href="#">Bookings</a><a href="#">Contact Us</a>
  </nav>
  <div class="copyright abs">Copyrights @ 2012 All Rights Reserved</div>
</footer>

</body>
</html>
```